Design the app for the next Dwelvo

We need a cutting edge, super UX-intuitive, design for a global parking app called Sloto.
- Homescreen and website have been finalised already (see attached pdf)
- Wireframed screens for the concepts we need have been provided in the attached pdf
- We need some really nice icons for parking space types, etc
- Needs to be very, very intuitive to use and navigate.
References: Dwelvo app & Zipto app, for their simplicity of use
Reason: A few designers have requested that we extend this deadline. So here you go.
Parking

```html
<!DOCTYPE html>
<html lang="en">
<head>
<meta charset="utf-8">
<title>How it works</title>
<link href="https://fonts.googleapis.com/css2?family=Lato:wght@300;400&display=swap" rel="stylesheet">
<style>
  :root {
    --backdrop-dark: #161616;
    --backdrop-mid: #3a3a3a;
    --card: #ffffff;
    --ink: #2a2a2a;
    --art-light: #e2e2e2;
    --art-mid: #b4b4b4;
    --dot: #8e8e8e;
    --accent: #d0101b;
  }
  * { margin: 0; padding: 0; box-sizing: border-box; }
  html, body { width: 675px; height: 1200px; overflow: hidden; }
  body { position: relative; font-family: "Lato", sans-serif; color: var(--ink); }

  .backdrop {
    position: absolute; inset: 0;
    background: radial-gradient(ellipse at 50% 55%, var(--backdrop-mid) 0%, var(--backdrop-dark) 75%);
  }

  .onboarding-card {
    position: absolute; left: 72px; top: 107px;
    width: 531px; height: 986px;
    background: var(--card); border-radius: 8px;
  }

  .close-button {
    position: absolute; left: 482px; top: 41px;
    width: 22px; height: 22px;
  }

  .eyebrow {
    position: absolute; top: 94px; width: 100%;
    text-align: center; font-weight: 300; font-size: 25.5px; letter-spacing: 0.5px;
  }

  .step-illustration {
    position: absolute; left: 110px; top: 162px;
    width: 311px; height: 311px; border-radius: 50%;
    background: radial-gradient(circle at 50% 40%, var(--art-light) 55%, var(--art-mid) 100%);
  }

  .step-title {
    position: absolute; top: 580px; width: 100%;
    text-align: center; font-weight: 400; font-size: 36px; letter-spacing: 0.3px;
  }

  .step-body {
    position: absolute; top: 694px; width: 100%;
    text-align: center; font-weight: 400; font-size: 26px; line-height: 31px;
  }

  .pager {
    position: absolute; top: 947px; width: 100%;
    display: flex; justify-content: center; gap: 10px;
  }
  .pager-dot { width: 9px; height: 9px; border-radius: 50%; background: var(--dot); }
  .pager-dot.is-active { background: var(--accent); }
</style>
</head>
<body>
  <div class="backdrop" role="img" aria-label="Blurred black and white photo of a street parking sign"></div>

  <section class="onboarding-card">
    <svg class="close-button" viewBox="0 0 22 22" aria-label="Close">
      <path d="M1 1 L21 21 M21 1 L1 21" stroke="#2a2a2a" stroke-width="2.4" fill="none"/>
    </svg>

    <p class="eyebrow">HOW IT WORKS</p>

    <div class="step-illustration" role="img" aria-label="Illustration of a map pin holding a car above a winding road"></div>

    <h1 class="step-title">PARK YOUR VEHICLE</h1>

    <p class="step-body">Save time. Spend less. Sleep easy.<br>Your vehicle now has its own pri-<br>vate parking space.</p>

    <div class="pager">
      <span class="pager-dot"></span>
      <span class="pager-dot is-active"></span>
      <span class="pager-dot"></span>
    </div>
  </section>
</body>
</html>
```